Kesrow Consulting- executive coaching business

looking for business card design for a newly started coaching business.
specialising in Exective coaching, Leadership, NLP and Motivation.
Looking for a simple, classy design using the existing logo attached and colour themes that complement the logo.
No red or orange in the business card design please.

Target Market(s)

Defence and Veteran community

Industry/Entity Type

Life Coaching

Contact Information for Business Card

looking for business cards for newly started coaching business.
specialising in Exective Coaching, Leadership, NLP and Motivation

Font styles to use
Serif
Script

Colors
0556a4
3176b5
86cfc6
33b8a4

Requirements
Must have
• Logo
• Email address- Lena@kesrowconsulting.com.au
• Contact number
• Services provided - Executive Coaching, Leadership, NLP and Motivational Mapping.
Nice to have
• Same colours as logo
Should not have
• Red or orange

```html
<!DOCTYPE html>
<html lang="en">
<head>
<meta charset="utf-8">
<title>Kesrow Consulting – Business Card</title>
<link rel="stylesheet" href="https://fonts.googleapis.com/css2?family=Montserrat:wght@500;600;700&family=Open+Sans:wght@600;700&display=swap">
<style>
  :root {
    --blue-deep: #0b4f9c;
    --blue-mid: #1f63b3;
    --blue-light: #3176b5;
    --green: #33b8a4;
    --green-bright: #3ab878;
    --teal-soft: #86cfc6;
    --paper: #f4f4f4;
    --grey-text: #8c8c8c;
    --stage: #e6e6e6;
    --white: #ffffff;
  }
  * { margin: 0; padding: 0; box-sizing: border-box; }
  html, body { width: 1200px; height: 799px; overflow: hidden; }
  body {
    background: var(--stage);
    font-family: "Open Sans", Arial, sans-serif;
    position: relative;
  }
  .card {
    position: absolute;
    top: 240px;
    width: 540px;
    height: 310px;
    border-radius: 28px;
    overflow: hidden;
    box-shadow: 0 10px 24px rgba(0,0,0,0.18);
  }

  /* Back of card */
  .card-back {
    left: 30px;
    background: radial-gradient(ellipse at 60% 40%, var(--blue-light), var(--blue-mid) 45%, var(--blue-deep));
    color: var(--white);
  }
  .card-back .ridge-art {
    position: absolute;
    left: 40px; top: 70px;
    width: 480px; height: 220px;
    background: linear-gradient(160deg, rgba(51,184,164,0) 10%, rgba(51,184,164,0.35) 50%, rgba(51,184,164,0) 90%);
    border-radius: 40% 60% 0 0;
  }
  .services {
    position: absolute;
    left: 34px; top: 42px;
    font-size: 13px;
    font-weight: 700;
    line-height: 1.3;
  }
  .services .services-title { color: var(--green-bright); }
  .back-brand {
    position: absolute;
    left: 0; right: 0; top: 150px;
    text-align: center;
  }
  .brand-name {
    font-family: "Montserrat", Arial, sans-serif;
    font-weight: 600;
    letter-spacing: 0.5px;
  }
  .brand-dot {
    display: inline-block;
    border-radius: 50%;
  }
  .back-brand .brand-name {
    font-size: 32px;
    color: var(--white);
    display: inline-flex;
    align-items: center;
    gap: 12px;
  }
  .back-brand .brand-dot { width: 34px; height: 34px; border: 3px solid var(--white); }
  .back-web {
    margin-top: 16px;
    font-size: 13px;
    font-weight: 600;
  }

  /* Front of card */
  .card-front {
    left: 630px;
    background: var(--paper);
  }
  .card-front svg.panel { position: absolute; inset: 0; }
  .front-brand {
    position: absolute;
    left: 22px; top: 72px;
    width: 206px;
    text-align: center;
  }
  .front-brand .brand-dot { width: 36px; height: 36px; border: 3px solid var(--grey-text); }
  .front-brand .brand-name {
    margin-top: 8px;
    font-size: 24px;
    line-height: 1.15;
    color: var(--blue-mid);
  }
  .front-brand .brand-rule {
    margin: 10px auto 0;
    height: 2px;
    width: 190px;
    background: var(--green-bright);
  }
  .holder {
    position: absolute;
    right: 26px; top: 34px;
    text-align: right;
    color: var(--white);
  }
  .holder-name { font-size: 18px; font-weight: 700; }
  .holder-role { font-size: 12px; font-weight: 600; }
  .contact {
    position: absolute;
    right: 24px; bottom: 26px;
    list-style: none;
    text-align: right;
    color: var(--white);
    font-size: 12px;
    font-weight: 600;
    line-height: 1.45;
  }
  .contact li { display: flex; justify-content: flex-end; align-items: center; gap: 8px; }
  .contact .icon {
    width: 12px; height: 12px;
    border-radius: 50%;
    background: var(--white);
    flex: none;
  }
  .contact .no-icon { width: 12px; flex: none; }
</style>
</head>
<body>

  <section class="card card-back" aria-label="Card back">
    <div class="ridge-art" role="img" aria-label="Faint mountain ridge decoration in teal"></div>
    <div class="services">
      <div class="services-title">Services provided:</div>
      <div>Executive Coaching</div>
      <div>Leadership</div>
      <div>NLP and Motivational Mapping</div>
    </div>
    <div class="back-brand">
      <div class="brand-name"><span class="brand-dot"></span>KESROW CONSULTING</div>
      <div class="back-web">www.kesrowconsulting.com.au</div>
    </div>
  </section>

  <section class="card card-front" aria-label="Card front">
    <svg class="panel" width="540" height="310" viewBox="0 0 540 310" aria-hidden="true">
      <defs>
        <radialGradient id="blueFill" cx="70%" cy="40%" r="70%">
          <stop offset="0" stop-color="#3176b5"/>
          <stop offset="0.5" stop-color="#1f63b3"/>
          <stop offset="1" stop-color="#0b4f9c"/>
        </radialGradient>
      </defs>
      <path d="M300 0 L540 0 L540 310 L250 310 L250 150 Q250 128 272 116 Q300 100 300 78 Z" fill="url(#blueFill)"/>
      <path d="M300 0 L300 78 Q300 100 272 116 Q250 128 250 150 L250 310" fill="none" stroke="#ffffff" stroke-width="12"/>
      <path d="M290 0 L290 76 Q290 96 264 110 Q240 124 240 148 L240 310" fill="none" stroke="#3ab878" stroke-width="4"/>
      <path d="M0 0 L40 0 Q30 30 0 40 Z" fill="#0b4f9c"/>
    </svg>
    <div class="front-brand">
      <span class="brand-dot"></span>
      <div class="brand-name">KESROW<br>CONSULTING</div>
      <div class="brand-rule"></div>
    </div>
    <div class="holder">
      <div class="holder-name">Mara Ellison</div>
      <div class="holder-role">President</div>
    </div>
    <ul class="contact">
      <li>#48, Ridgeway Lane<span class="no-icon"></span></li>
      <li>Summit Vale, Australia<span class="no-icon"></span></li>
      <li>402.118.730<span class="icon"></span></li>
      <li>402.553.961<span class="icon"></span></li>
      <li>402.774.205<span class="icon"></span></li>
      <li>Lena@kesrowconsulting.com.au<span class="icon"></span></li>
      <li>www.kesrowconsulting.com.au<span class="icon"></span></li>
    </ul>
  </section>

</body>
</html>
```